Vita Shield Prime is a new Chinese herbal medicine nutritional supplement.

I need a label design for my Dr Penwick Rx Chinese herbal supplement line .
I am launching a new super powerful immune booster
Vita Shield Prime.
The FRONT label 3 in. x 4 in. Black mylar bag will have 30 capsules
The Back label will be the size 3 inches x 3 inches will send information
Target Market(s)
Females 25 to 80 who buy nutritional supplements for themselves and their families.
Industry/Entity Type
Medicine
Font styles to use
Decorative
Colors
Designer to choose colors to be used in the design.
Requirements
Must have
- Dr Penwick Rx the name of the company. A wax seal with the an imprint of the name stamp letters on wax .. examples will be provided below.. an image of name stamp inside wax seal. Product name is Vita Shield Prime. Must use traditional Chinese colors. COLORS BELOW IN SAVED IMAGES.. GOLD, BLOOD RED, DARK PURPLE. description of product... Powerful Immune Booster.. a clear and easy to read label. ALL SO BACK LABEL 3 INCHES X 3 INCHES USING ONLY TWO COLORS.. BASIC PRODUCT LABEL OF INGREDIENTS, SUGGESTED USE, PRODUCT INFO, AND WARNINGS. IMAGES FILE 3 IS TO BE USED IN WAX SEAL.USE ONLY EXAMPLE COLORS BELOW IN IMAGES
Nice to have
- I like royal colors of ancient China, which happen to be strong psychological colors for marketing. A Gold wax with my name stamp in red or something like that. "Ancient Chinese secret for modern health".
Should not have

```html
<!DOCTYPE html>
<html lang="en">
<head>
<meta charset="utf-8">
<title>Vita Shield Prime – Label Colour Options</title>
<link rel="stylesheet" href="https://fonts.googleapis.com/css2?family=Alegreya:wght@500&family=Saira:ital,wght@1,800;1,900&display=swap">
<style>
  :root {
    --page: #ffffff;
    --frame: #9a9a9a;
    --blood-red: #d93208;
    --royal-purple: #4a2e63;
    --gold-dark: #a98a45;
    --gold-light: #f2e28f;
    --label-white: #ffffff;
    --ink: #2f2f2f;
    --option-number: #8f8f8f;
  }
  html, body {
    margin: 0;
    padding: 0;
    width: 986px;
    height: 1200px;
    overflow: hidden;
    background: var(--page);
  }
  .sheet {
    position: relative;
    width: 986px;
    height: 1200px;
    box-sizing: border-box;
    border: 1px solid var(--frame);
  }
  .label-option {
    position: absolute;
    width: 402px;
    height: 538px;
  }
  .label-option svg { display: block; width: 100%; height: 100%; }
  .option-a { left: 94px;  top: 18px; }
  .option-b { left: 529px; top: 18px; }
  .option-c { left: 94px;  top: 615px; }
  .option-d { left: 529px; top: 615px; }

  .option-number {
    position: absolute;
    font-family: Arial, Helvetica, sans-serif;
    font-size: 38px;
    color: var(--option-number);
    line-height: 1;
  }
  .num-a { left: 45px;  top: 522px; }
  .num-b { left: 936px; top: 504px; }
  .num-c { left: 58px;  top: 1080px; }
  .num-d { left: 930px; top: 1080px; }

  .bg-red { fill: var(--blood-red); }
  .label-field { fill: var(--label-white); }
  .band-purple { fill: var(--royal-purple); }
  .band-red { fill: var(--blood-red); }

  .company-name {
    font-family: "Alegreya", Georgia, serif;
    font-weight: 500;
    font-size: 37px;
    fill: var(--ink);
  }
  .product-line, .product-word, .tagline {
    font-family: "Saira", "Arial Black", sans-serif;
    font-style: italic;
  }
  .product-line { font-weight: 800; font-size: 33px; letter-spacing: 0.5px; }
  .product-word { font-weight: 900; font-size: 58px; letter-spacing: 1px; }
  .on-gold { fill: var(--ink); }
  .on-color { fill: var(--label-white); }
  .tagline { font-weight: 800; font-size: 31px; fill: var(--ink); letter-spacing: 1px; }
</style>
</head>
<body>
<main class="sheet">

  <svg width="0" height="0" style="position:absolute" aria-hidden="true">
    <defs>
      <linearGradient id="gold-foil" x1="0" y1="0" x2="1" y2="0">
        <stop offset="0" stop-color="#a98a45"/>
        <stop offset="0.35" stop-color="#e8cf7e"/>
        <stop offset="0.7" stop-color="#f2e28f"/>
        <stop offset="1" stop-color="#b69a50"/>
      </linearGradient>
      <radialGradient id="wax" cx="0.4" cy="0.35" r="0.7">
        <stop offset="0" stop-color="#f05a22"/>
        <stop offset="0.7" stop-color="#d93208"/>
        <stop offset="1" stop-color="#a82404"/>
      </radialGradient>
    </defs>
  </svg>

  <!-- Option A: gold ground, gold band -->
  <section class="label-option option-a">
    <svg viewBox="0 0 397 532">
      <rect width="397" height="532" fill="url(#gold-foil)"/>
      <path class="label-field" d="M12,250 C12,135 95,57 198.5,57 C302,57 385,135 385,250 V360 C385,445 302,510 198.5,510 C95,510 12,445 12,360 Z"/>
      <rect x="12" y="259" width="373" height="100" fill="url(#gold-foil)"/>
      <circle cx="204" cy="103" r="72" fill="url(#wax)" role="img" aria-label="Red wax seal stamped with the company initials"/>
      <text class="company-name" x="199" y="238" text-anchor="middle">Dr Penwick Rx’s</text>
      <text class="product-line on-gold" x="199" y="296" text-anchor="middle">VITA SHIELD</text>
      <text class="product-word on-gold" x="199" y="348" text-anchor="middle">PRIME</text>
      <text class="tagline" x="113" y="393">Powerful</text>
      <text class="tagline" x="113" y="432">Immune</text>
      <text class="tagline" x="113" y="470">Booster.</text>
    </svg>
  </section>
  <span class="option-number num-a">1</span>

  <!-- Option B: red ground, gold band -->
  <section class="label-option option-b">
    <svg viewBox="0 0 397 532">
      <rect class="bg-red" width="397" height="532"/>
      <path class="label-field" d="M12,250 C12,135 95,57 198.5,57 C302,57 385,135 385,250 V360 C385,445 302,510 198.5,510 C95,510 12,445 12,360 Z"/>
      <rect x="12" y="259" width="373" height="100" fill="url(#gold-foil)"/>
      <circle cx="204" cy="103" r="72" fill="url(#wax)" role="img" aria-label="Red wax seal stamped with the company initials"/>
      <text class="company-name" x="199" y="238" text-anchor="middle">Dr Penwick Rx’s</text>
      <text class="product-line on-gold" x="199" y="296" text-anchor="middle">VITA SHIELD</text>
      <text class="product-word on-gold" x="199" y="348" text-anchor="middle">PRIME</text>
      <text class="tagline" x="113" y="393">Powerful</text>
      <text class="tagline" x="113" y="432">Immune</text>
      <text class="tagline" x="113" y="470">Booster.</text>
    </svg>
  </section>
  <span class="option-number num-b">2</span>

  <!-- Option C: red ground, purple band -->
  <section class="label-option option-c">
    <svg viewBox="0 0 397 532">
      <rect class="bg-red" width="397" height="532"/>
      <path class="label-field" d="M12,250 C12,135 95,57 198.5,57 C302,57 385,135 385,250 V360 C385,445 302,510 198.5,510 C95,510 12,445 12,360 Z"/>
      <rect class="band-purple" x="12" y="259" width="373" height="98"/>
      <circle cx="204" cy="103" r="72" fill="url(#wax)" role="img" aria-label="Red wax seal stamped with the company initials"/>
      <text class="company-name" x="199" y="238" text-anchor="middle">Dr Penwick Rx’s</text>
      <text class="product-line on-color" x="199" y="296" text-anchor="middle">VITA SHIELD</text>
      <text class="product-word on-color" x="199" y="348" text-anchor="middle">PRIME</text>
      <text class="tagline" x="113" y="393">Powerful</text>
      <text class="tagline" x="113" y="432">Immune</text>
      <text class="tagline" x="113" y="470">Booster.</text>
    </svg>
  </section>
  <span class="option-number num-c">3</span>

  <!-- Option D: red ground, red band -->
  <section class="label-option option-d">
    <svg viewBox="0 0 397 532">
      <rect class="bg-red" width="397" height="532"/>
      <path class="label-field" d="M12,250 C12,135 95,57 198.5,57 C302,57 385,135 385,250 V360 C385,445 302,510 198.5,510 C95,510 12,445 12,360 Z"/>
      <rect class="band-red" x="12" y="259" width="373" height="98"/>
      <circle cx="204" cy="103" r="72" fill="url(#wax)" role="img" aria-label="Red wax seal stamped with the company initials"/>
      <text class="company-name" x="199" y="238" text-anchor="middle">Dr Penwick Rx’s</text>
      <text class="product-line on-color" x="199" y="296" text-anchor="middle">VITA SHIELD</text>
      <text class="product-word on-color" x="199" y="348" text-anchor="middle">PRIME</text>
      <text class="tagline" x="113" y="393">Powerful</text>
      <text class="tagline" x="113" y="432">Immune</text>
      <text class="tagline" x="113" y="470">Booster.</text>
    </svg>
  </section>
  <span class="option-number num-d">4</span>

</main>
</body>
</html>
```